Postcard Design for Birchfield Medical Center Integrated Medicine

We need a postcard that we will be able to hand out at events that gives an overview of what we do at Birchfield Medical Center. Birchfield Medical Center, located in Encinitas, California, is an integrated medical center using functional medicine to prevent and reverse chronic diseases. We would also like to highly emphasize that we take Medicare and PPO insurance for these services and if patients have any questions to contact the front desk.

The attached screenshots are elementary versions of what we hope our postcard will have.

THIS IS NOT INTENDED TO BE MAILED SO AN ADDRESS SPACE IS NOT NEEDED
ALSO, WE WOULD LIKE TO HAVE THIS SIZE 6X4

Birchfieldmedcenter.net is our website if you would need any further information about the company.

```html
<!DOCTYPE html>
<html lang="en">
<head>
<meta charset="utf-8">
<title>Birchfield Medical Center – Integrated Medicine Postcard</title>
<link rel="stylesheet" href="https://fonts.googleapis.com/css2?family=Questrial&family=Montserrat:wght@600&display=swap">
<style>
  :root {
    --ink: #6d6e71;
    --ink-dark: #58595b;
    --teal: #2fb3c9;
    --teal-soft: #cfe9ee;
    --band-gray: #b5b6b9;
    --line-gray: #8a8b8e;
    --paper: #ffffff;
    --mist: #e9eef4;
  }
  * { margin: 0; padding: 0; box-sizing: border-box; }
  html, body { width: 1200px; height: 800px; overflow: hidden; background: var(--paper); }
  .postcard {
    position: relative;
    width: 1200px;
    height: 800px;
    overflow: hidden;
    font-family: "Questrial", sans-serif;
    color: var(--ink);
    background:
      radial-gradient(ellipse at 25% 20%, #ffffff 0%, rgba(255,255,255,0) 55%),
      radial-gradient(ellipse at 80% 35%, #ffffff 0%, rgba(255,255,255,0) 45%),
      linear-gradient(160deg, #f4f7fa 0%, var(--mist) 45%, #f1f4f8 100%);
  }
  .intro {
    position: absolute;
    left: 46px;
    top: 79px;
    width: 660px;
    font-size: 23px;
    letter-spacing: 0.4px;
    line-height: 26.5px;
  }
  .conditions {
    position: absolute;
    left: 46px;
    top: 222px;
    display: grid;
    grid-template-columns: 378px 300px;
    font-size: 17px;
    letter-spacing: 0.4px;
    line-height: 20px;
  }
  .conditions ul { list-style: none; }
  .insurance {
    position: absolute;
    left: 46px;
    top: 462px;
    font-size: 23px;
    letter-spacing: 0.4px;
    line-height: 28px;
  }
  .brand {
    position: absolute;
    left: 740px;
    top: 250px;
    width: 380px;
    display: flex;
    align-items: center;
    gap: 22px;
  }
  .brand-dot {
    flex: none;
    width: 58px;
    height: 58px;
    border-radius: 50%;
    background: var(--teal);
  }
  .brand-name {
    font-size: 36px;
    line-height: 42px;
    color: var(--teal);
  }
  .waves {
    position: absolute;
    left: 0;
    top: 0;
    width: 1200px;
    height: 800px;
  }
  .footer-name {
    position: absolute;
    left: 46px;
    top: 722px;
    font-family: "Montserrat", sans-serif;
    font-weight: 600;
    font-size: 26px;
    color: var(--ink-dark);
  }
  .footer-divider {
    position: absolute;
    left: 584px;
    top: 690px;
    width: 2px;
    height: 92px;
    background: var(--band-gray);
  }
  .contact {
    position: absolute;
    left: 608px;
    top: 698px;
    list-style: none;
    font-size: 22px;
    letter-spacing: 0.3px;
    line-height: 34px;
  }
  .contact li { display: flex; align-items: center; gap: 10px; }
  .contact svg { width: 18px; height: 18px; fill: var(--ink); }
</style>
</head>
<body>
<main class="postcard">
  <svg class="waves" viewBox="0 0 1200 800" aria-hidden="true">
    <path d="M0 690 Q600 700 1200 520 L1200 800 L0 800 Z" fill="var(--paper)"/>
    <path d="M40 628 Q150 585 360 585 Q560 588 660 628 Z" fill="var(--teal-soft)"/>
    <path d="M12 622 Q600 660 1188 512 L1188 522 Q620 690 12 678 Z" fill="var(--band-gray)"/>
    <path d="M12 690 Q640 700 1188 532" fill="none" stroke="var(--line-gray)" stroke-width="3"/>
  </svg>

  <p class="intro">Treating root causes not symptoms by using a whole system approach to medicine, preventig and reserving chronic conditions and disease. Ultimately, creating optimal health and vitality. Some of the conditions we treat are...</p>

  <div class="conditions">
    <ul>
      <li>Acne</li>
      <li>Diabetes</li>
      <li>Depression/ Anxiety</li>
      <li>Healthy Aging</li>
      <li>Parkinson’s Disease</li>
      <li>Sleep Insomia</li>
      <li>Healthy Weight and Metabolism</li>
      <li>Cancer Prevention</li>
      <li>Thyroid/ Adrenal Disorders</li>
      <li>Arthritis</li>
    </ul>
    <ul>
      <li>Ashthma</li>
      <li>Dextoxification and Healing</li>
      <li>Migraines and Headaches</li>
      <li>Chronic Fatique</li>
      <li>Autoimmune Diseases</li>
      <li>Food Allergies</li>
      <li>Female Disorders</li>
      <li>Hormone Imbalance</li>
      <li>Osteoporosis</li>
      <li>And many more</li>
    </ul>
  </div>

  <p class="insurance">We accept all Medicare and PPO insurance.<br>Please contact the Front Desk for more information.</p>

  <div class="brand">
    <span class="brand-dot"></span>
    <p class="brand-name">Birchfield Medical Center Integrated Medicine</p>
  </div>

  <p class="footer-name">Dr. Renata Ellsworth, M.D. ABAARM</p>
  <span class="footer-divider"></span>
  <ul class="contact">
    <li>
      <svg viewBox="0 0 24 24" aria-hidden="true"><path d="M6.6 10.8a15.1 15.1 0 0 0 6.6 6.6l2.2-2.2a1 1 0 0 1 1-.25 11.4 11.4 0 0 0 3.6.57 1 1 0 0 1 1 1V20a1 1 0 0 1-1 1A17 17 0 0 1 3 4a1 1 0 0 1 1-1h3.5a1 1 0 0 1 1 1c0 1.25.2 2.45.57 3.57a1 1 0 0 1-.25 1z"/></svg>
      <span>760-555-0142</span>
    </li>
    <li>
      <svg viewBox="0 0 24 24" aria-hidden="true"><path d="M12 2a7 7 0 0 0-7 7c0 5.250 7 13 7 13s7-7.75 7-13a7 7 0 0 0-7-7zm0 9.5A2.5 2.5 0 1 1 12 6.5a2.5 2.5 0 0 1 0 5z"/></svg>
      <span>418 Harbor View Rd # 100, Larkspur Bay, CA 90099</span>
    </li>
  </ul>
</main>
</body>
</html>
```